Create a Graphic About YOURSELF and PixelHarbor

PixelHarbor would like you (designers) to create an awesome graphic to promote YOURSELF and your profile on PixelHarbor!

Your graphic should communicate your name, your services and should mention PixelHarbor.

The design should be perfect for sharing on Chatterly. Here's an example of what we'd like http://blog.pixelharbor-example.ca/article/333/pixelharbor-launches-3000-hire-me-social-design-contest

Once you submitted your design, we'd love you to share the design ('advertisement') and promote yourself and PixelHarbor to your friends and potential customers. So make your submissions great and get your friends to vote for your design by 'Liking' it on Chatterly!

Prizes:
$1500 - "PixelHarbor Community" prize awarded to the designer with the most Chatterly 'Likes'
5 x $50 for the next 5 'most liked' designs on Chatterly

$1000 - "Hire Me" prize awarded to the designer who receives the most client invites
5 x $50 for the next 5 'most invited' designers

In summary, this is a great opportunity for you to increase your exposure to PixelHarbor customers and win cash prizes. Show off your design skills and get hired by PixelHarbor customers from around the world!

Target Market(s)

Fans, friends and customers of YOU

Industry/Entity Type

Cash

Requirements
Must have
• 1) Include your PixelHarbor user name on the graphic so customers can find you in the PixelHarbor Designer Directory
2) Include the tagline "Hire Me on PixelHarbor.com!" in your graphic design.
3) Share your design's URL on our Chatterly wall at http://chatterly-example.com/pixelharbor and get your friends to 'like' your design.
Nice to have
• 1) Include a tagline that expresses your design approach/philosophy
2) Artwork dimensions: 403 x 403 px
3) You can submit more than 1 design!
Should not have
• You must own the copyright of any images you use including stock imagery.

```html
<!DOCTYPE html>
<html lang="en">
<head>
<meta charset="utf-8">
<title>vexlo works – design services</title>
<link rel="stylesheet" href="https://fonts.googleapis.com/css2?family=Comfortaa:wght@400;700&display=swap">
<style>
  :root {
    --leather-light: #5a4836;
    --leather-mid: #46382a;
    --leather-dark: #241c15;
    --ink-service: #d9caa9;
    --ink-name: #f1e9da;
    --ink-name-shade: #1a130d;
    --badge-fill: #3b3026;
    --badge-ring: #9a9088;
    --plane-red: #b23a24;
    --plane-cream: #d8d0b8;
  }
  * { margin: 0; padding: 0; box-sizing: border-box; }
  html, body { width: 1200px; height: 1200px; overflow: hidden; background: var(--leather-dark); }
  .canvas {
    position: relative;
    width: 1200px;
    height: 1200px;
    overflow: hidden;
    background:
      radial-gradient(ellipse 70% 65% at 50% 45%, var(--leather-light) 0%, var(--leather-mid) 55%, var(--leather-dark) 100%);
    font-family: "Comfortaa", sans-serif;
  }
  .word {
    position: absolute;
    transform: translate(-50%, -50%) rotate(-11deg);
    color: var(--ink-service);
    white-space: nowrap;
    line-height: 1;
    font-weight: 400;
    text-shadow: 0 2px 3px rgba(0,0,0,.45);
  }
  .word--logotype  { left: 920px;  top: 225px; font-size: 82px; }
  .word--flyers    { left: 910px;  top: 388px; font-size: 54px; }
  .word--print     { left: 995px;  top: 706px; font-size: 100px; }
  .word--web       { left: 213px;  top: 828px; font-size: 86px; }
  .word--design    { left: 274px;  top: 900px; font-size: 86px; }
  .word--brochures { left: 669px;  top: 866px; font-size: 46px; }
  .word--posters   { left: 203px;  top: 1090px; font-size: 46px; }
  .word--banners   { left: 645px;  top: 1108px; font-size: 46px; }

  .tagline {
    position: absolute;
    left: 905px;
    top: 78px;
    transform: translate(-50%, -50%) rotate(-11deg);
    color: var(--ink-service);
    font-size: 30px;
    font-weight: 400;
    white-space: nowrap;
    line-height: 1;
    text-shadow: 0 2px 3px rgba(0,0,0,.45);
  }

  .studio-name {
    position: absolute;
    color: var(--ink-name);
    font-weight: 700;
    font-size: 112px;
    line-height: 1;
    white-space: nowrap;
    transform: translate(-50%, -50%) rotate(-10deg);
    text-shadow: 0 5px 6px var(--ink-name-shade);
  }
  .studio-name--first  { left: 490px; top: 560px; }
  .studio-name--second { left: 732px; top: 632px; }

  .badge {
    position: absolute;
    left: 330px;
    top: 90px;
    transform: translateX(-50%);
    display: flex;
    flex-direction: column;
    align-items: center;
    gap: 14px;
  }
  .badge__mark { width: 190px; height: 190px; flex: none; }
  .badge__name {
    color: var(--ink-service);
    font-weight: 400;
    font-size: 42px;
    line-height: 1;
    white-space: nowrap;
  }
  .badge__user {
    color: var(--ink-service);
    font-weight: 400;
    font-size: 22px;
    line-height: 1;
    white-space: nowrap;
  }

  .plane-art {
    position: absolute;
    left: 790px;
    top: 920px;
    width: 330px;
    height: 150px;
  }
</style>
</head>
<body>
<main class="canvas">
  <div class="badge">
    <svg class="badge__mark" viewBox="0 0 190 190" aria-hidden="true">
      <circle cx="95" cy="95" r="88" fill="var(--badge-fill)" stroke="var(--badge-ring)" stroke-width="8"/>
    </svg>
    <span class="badge__name">vexlo works</span>
    <span class="badge__user">PixelHarbor user: vexloworks</span>
  </div>

  <p class="tagline">Hire Me on PixelHarbor.com!</p>

  <span class="word word--logotype">logotype</span>
  <span class="word word--flyers">flyers</span>

  <h1 class="studio-name studio-name--first">vexlo</h1>
  <span class="studio-name studio-name--second">works</span>

  <span class="word word--print">print</span>
  <span class="word word--web">web</span>
  <span class="word word--design">design</span>
  <span class="word word--brochures">brochures</span>
  <span class="word word--posters">posters</span>
  <span class="word word--banners">banners</span>

  <svg class="plane-art" viewBox="0 0 330 150" role="img" aria-label="Illustration of a small red propeller biplane flying right with a white smoke trail">
    <defs>
      <linearGradient id="plane-tone" x1="0" y1="0" x2="1" y2="0">
        <stop offset="0" stop-color="var(--plane-cream)" stop-opacity="0"/>
        <stop offset="0.55" stop-color="var(--plane-cream)" stop-opacity="0.35"/>
        <stop offset="1" stop-color="var(--plane-red)" stop-opacity="0.75"/>
      </linearGradient>
    </defs>
    <rect x="0" y="20" width="330" height="110" rx="55" fill="url(#plane-tone)"/>
  </svg>
</main>
</body>
</html>
```